New retail box design

We are looking at changing our packaging for retilers. I have templates of boxes and like a great design for new packaging.

I will attach pictures of our current packaging.

Industry/Entity Type

Ammunition manufacturing

Requirements
Must have
• warning label and company name

```html
<!DOCTYPE html>
<html lang="en">
<head>
<meta charset="utf-8">
<title>Liberty Forge Cartridge Co. – Retail Box Dieline</title>
<link rel="stylesheet" href="https://fonts.googleapis.com/css2?family=Lora:wght@400;600;700&display=swap">
<style>
  :root {
    --paper: #ffffff;
    --navy: #0d0f22;
    --crimson: #82141b;
    --ink-red: #e8313a;
    --text-light: #f2f2f2;
    --text-muted: #d6d6d6;
    --panel-black: #0b0b0c;
    --panel-grey: #3b3b3d;
    --cut-line: #9a9aa6;
  }
  * { margin: 0; padding: 0; box-sizing: border-box; }
  html, body {
    width: 1200px; height: 849px; overflow: hidden;
    background: var(--paper);
    font-family: "Lora", Georgia, serif;
  }
  .dieline { position: relative; width: 1200px; height: 849px; }
  .dieline-art { position: absolute; inset: 0; }

  .warning-card {
    position: absolute; left: 193px; top: 353px; width: 223px; height: 200px;
    border: 1.4px solid var(--text-light); border-radius: 10px;
  }
  .warning-title {
    position: absolute; left: 0; right: 0; top: 8px;
    text-align: center; color: var(--ink-red);
    font-size: 11.4px; font-weight: 600;
  }
  .warning-subtitle {
    position: absolute; left: 0; right: 0; top: 22px;
    text-align: center; color: var(--ink-red);
    font-size: 8px; font-weight: 600;
  }
  .warning-rule {
    position: absolute; left: 9px; right: 8px; top: 41px;
    height: 1.3px; background: var(--ink-red);
  }
  .safety-rules {
    position: absolute; left: 196px; top: 405px; width: 218px;
    list-style: none; color: var(--text-light);
    font-size: 6.4px; font-weight: 700; line-height: 10px;
  }
  .safety-rules li { position: relative; padding-left: 11px; margin-bottom: 4.6px; }
  .safety-rules li::before {
    content: ""; position: absolute; left: 0; top: 2.5px;
    width: 5px; height: 5px; border-radius: 50%;
    border: 1px solid var(--ink-red);
    background: radial-gradient(circle, var(--ink-red) 45%, transparent 50%);
  }

  .lead-warning {
    position: absolute; left: 431px; top: 350px; width: 170px;
    color: var(--text-light); font-size: 8.9px; line-height: 11px;
  }
  .lead-warning p { margin-bottom: 8.5px; }
  .lead-warning .label { color: var(--ink-red); }

  .brand-name {
    position: absolute; color: var(--ink-red);
    font-size: 12px; font-weight: 700; white-space: nowrap;
  }
  .brand-name--lid {
    left: 220px; top: 238px; width: 170px; text-align: center;
    transform: rotate(180deg);
  }
  .brand-name--front { left: 868px; top: 498px; width: 150px; text-align: center; font-size: 10.5px; }
  .brand-line {
    position: absolute; left: 862px; top: 535px; width: 150px; text-align: center;
    color: var(--text-muted); font-size: 10.3px; font-weight: 600; white-space: nowrap;
  }
</style>
</head>
<body>
<main class="dieline">
  <svg class="dieline-art" width="1200" height="849" viewBox="0 0 1200 849" xmlns="http://www.w3.org/2000/svg">
    <defs>
      <radialGradient id="flap-top" cx="0.5" cy="0" r="1">
        <stop offset="0" stop-color="#8d161d"/>
        <stop offset="0.55" stop-color="#4a0f1a"/>
        <stop offset="1" stop-color="var(--navy)"/>
      </radialGradient>
      <radialGradient id="flap-bottom" cx="0.5" cy="0.95" r="0.9">
        <stop offset="0" stop-color="#8a171c"/>
        <stop offset="0.55" stop-color="#3f0d18"/>
        <stop offset="1" stop-color="var(--navy)"/>
      </radialGradient>
      <radialGradient id="side-flap" cx="0.5" cy="0.3" r="0.9">
        <stop offset="0" stop-color="#6e1019"/>
        <stop offset="1" stop-color="var(--navy)"/>
      </radialGradient>
      <linearGradient id="pistol-photo" x1="0" y1="0" x2="1" y2="1">
        <stop offset="0" stop-color="#1a1a1b"/>
        <stop offset="0.45" stop-color="var(--panel-grey)"/>
        <stop offset="1" stop-color="#121213"/>
      </linearGradient>
      <radialGradient id="back-panel" cx="0.35" cy="0.45" r="0.8">
        <stop offset="0" stop-color="#4a4a4c"/>
        <stop offset="1" stop-color="var(--panel-black)"/>
      </radialGradient>
      <linearGradient id="flag-photo" x1="0" y1="0" x2="1" y2="0">
        <stop offset="0" stop-color="#3a3f58"/>
        <stop offset="0.3" stop-color="#5e4a3a"/>
        <stop offset="0.55" stop-color="#5a2228"/>
        <stop offset="0.8" stop-color="#1e1a1c"/>
        <stop offset="1" stop-color="#080809"/>
      </linearGradient>
    </defs>

    <!-- lid tuck flap and lid -->
    <path class="tuck-flap" d="M191 149 Q192 108 215 86 L393 86 Q417 108 419 149 Z" fill="url(#flap-top)"/>
    <rect class="lid-panel" x="188" y="147" width="233" height="186" fill="url(#flap-top)"/>
    <path class="tuck-slot" d="M212 147 L397 147 L393 151 L216 151 Z" fill="var(--paper)"/>

    <!-- dust flaps top -->
    <path class="dust-flap" d="M421 218 L576 218 L596 305 L605 314 L605 333 L421 333 Z" fill="url(#flap-top)"/>
    <path class="dust-flap" d="M871 218 L1024 218 L1024 333 L841 333 L841 319 L851 308 Z" fill="url(#flap-top)"/>

    <!-- glue flap -->
    <path class="glue-flap" d="M142 346 L188 333 L188 566 L178 566 L142 530 Z" fill="url(#side-flap)"/>
    <path d="M132 338 L179 326 L179 330 M133 524 L179 570 L179 560" fill="none" stroke="var(--cut-line)" stroke-width="0.6"/>

    <!-- main wrap panels -->
    <rect class="side-panel" x="188" y="333" width="233" height="233" fill="url(#pistol-photo)" role="img" aria-label="Photo of a handgun and scattered cartridges on a dark surface"/>
    <rect class="back-panel" x="421" y="333" width="184" height="233" fill="url(#back-panel)" role="img" aria-label="Dark surface with a single brass cartridge"/>
    <rect class="front-panel" x="605" y="333" width="419" height="233" fill="url(#flag-photo)" role="img" aria-label="Rifle cartridges standing before a waving stars and stripes flag"/>

    <!-- bottom flaps -->
    <path class="bottom-flap" d="M188 566 L421 566 L409 580 L416 585 L416 705 L373 705 L303 659 L303 668 L259 705 L200 705 Z" fill="url(#flap-bottom)"/>
    <path class="bottom-flap" d="M421 570 L606 566 L514 659 L442 659 L428 580 Z" fill="url(#flap-bottom)"/>
    <path class="bottom-flap" d="M608 566 L840 566 L826 580 L836 588 L836 705 L793 705 L722 659 L722 668 L678 705 L620 705 Z" fill="url(#flap-bottom)"/>
    <path class="bottom-flap" d="M846 566 L1024 566 L931 659 L861 659 Z" fill="url(#flap-bottom)"/>

    <!-- fold / score lines -->
    <g fill="none" stroke="var(--cut-line)" stroke-width="0.6">
      <path d="M409 580 L318 669"/>
      <path d="M428 580 L551 580 L551 610 L502 659"/>
      <path d="M826 580 L737 669"/>
      <path d="M846 580 L968 580 L968 610 L918 659"/>
    </g>
  </svg>

  <div class="brand-name brand-name--lid">Liberty Forge Cartridge Co.</div>

  <section class="warning-card">
    <h2 class="warning-title">Warning: Keep out of reach of children.</h2>
    <h3 class="warning-subtitle">Safety Rules:</h3>
    <div class="warning-rule"></div>
  </section>
  <ul class="safety-rules">
    <li>Watch your muzzle. Keep gun pointed in safe direction.</li>
    <li>Wear eye and ear protection.</li>
    <li>If gun fails to fire, keep it pointed in a safe direction, then unload carefully avoiding exposure to breech.</li>
    <li>Know your target and what is beyond it.</li>
    <li>Treat every gun as if it were loaded. Don't rely on the safety.</li>
    <li>Keep barrel clear of obstructions.</li>
    <li>Never load a gun until ready to use.</li>
    <li>Only use ammunition that exactly matches markings on your gun.</li>
  </ul>

  <section class="lead-warning">
    <p><span class="label">LEAD WARNING:</span> This product contains lead, a substance deemed hazardous to your health. A substance that has shown to be detrimental in birth defects, reproductive harm and other ailments causing serious physical harm, Use only in well ventilated areas.</p>
    <p>Wash hands immediately and thoroughly after use.</p>
    <p>Discharging firearms in poorly-ventilated areas, cleaning firearms or handling ammunition may result in exposure to lead and other substance known to cause birth defects, reproductive harm, cancer and other serious physical injury. Have adequate ventilation at all times. Wash hands after exposure.</p>
  </section>

  <div class="brand-name brand-name--front">Liberty Forge Cartridge Co.</div>
  <div class="brand-line">Liberty Forge Cartridge Co.</div>
</main>
</body>
</html>
```